Verpackungsdesign für italienische Produkte gesucht
Die Zusammenarbeit mit dem Designer 7Pixo hat sehr viel Spaß gemacht. Jeder Änderungswunsch wurde super schnell in die Tat umgesetzt. Die Kommunikation verlief reibungslos. Das Ergebnis ist einfach klasse geworden. Er hat ein großes Talent für den Entwurf von Designs. Ich freue mich sehr darauf, auch zukünftige Projekte mit ihm durchführen zu können. Vielen Dank nochmal an Ihn für die tolle Arbeit und die Unterstützung. Ich kann eine Zusammenabeit mit dem Designer 7Pixo nur empfehlen.
Liebe Designerinnen und Designer,
wir sind ein Unternehmen, welches Olivenöl, Pasta und Wein sowie Olivenblättertee und Tomatensoße auf Sizilien (Italien) in Gibellina produziert. In vierter Generation produziert die Familie Berardi landwirtschaftliche Erzeugnisse, die nach biologischen Prinzipien angebaut werden. Im Ackerbau verzichten wir auf synthetisch hergestellte Pflanzenschutzmittel, Mineraldünger und Grüne Gentechnik. Da in der heutigen Zeit viele Konsumenten den Ursprung der gekauften Produkte nicht mehr zurückverfolgen können und ihnen in dieser Hinsicht kaum Transparenz gewährleistet wird, möchten wir im Namen der Familie Berardi unseren Kunden den Herstellungsprozess vom Anbau bis zur Fertigstellung des Enderzeugnisses transparent aufzeigen und sie für die bewusste und gesunde Ernährung sensibilisieren.
Unsere Zielgruppe sind ernährungsbewusste Personen, überwiegend Frauen im mittleren Alter, die auf bewusste, gesunde Ernährung viel Wert legen.
Vielen lieben Dank für eure Arbeit im Voraus. Ich freue mich sehr auf die Designvorschläge.
Lieben Gruß
Marta & Lorenzo Berardi
KREATIVE DESIGNER gesucht
WIR SUCHEN EIN VERPACKUNGSKONZEPT FÜR UNSERE PRODUKTE
Für unsere Produkte: Olivenöl, Pasta und Wein sowie Olivenblättertee und Tomatensoße benötigen wir ein Verpackungsdesign, welches erkennen lässt, dass die Produkte zu einer Produktfamilie gehören. Darüber hinaus benötigen wir das Design für den Kartonanhänger, der an jedes unserer Produkte ran gehängt werden soll.
Erst einmal suchen wir nach Vorschlägen für ein Verpackungsdesign. Im Anschluss an dieses Projekt würden wir gerne mit dem Designer die Reinzeichnungen fertig erstellen. Den Preis für die Reinzeichnung würden wir dann gerne mit dem Designer verhandeln.
Mit dem Designer, der das Projekt gewinnt, streben wir auch nach dem Produktende eine enge Zusammenarbeit an, da sich unser Produktportfolio stetig erweitern wird und Folgeaufträge bereits in Planung sind.
Für die Produkte Olivenöl, Pasta und Tee sowie Tomatensoße benötigen wir Etiketten mit Vorder- und Rückseite. Für die Pasta-Verpackung soll ein Design für den Kartonreiter aus dünnem Kartonpapier erstellt werden (siehe Bild Pasta Design Beispiel). Dieses Kartonpapier könnte schwarz sein, da die Olivenölflasche, die Weinflaschen sowie die Verpackung für Tee und die Flasche für Tomatensoße ebenfalls dunkel sind.
Das Design sollte elegant und qualitativ hochwertig aussehen. Mit unseren Produkten sollen die folgenden Werte transportiert werden: Tradition, Familie, hochwertige Qualität, Transparenz, biologischer Anbau, bewusste Ernährung, Liebe zum Produkt, Sizilien,
Es sollten max. 4 verschiedene Farben verwendet werden.
In der Datei Vorgaben zum Design stehen weitere Angaben. Zusätzlich besteht eine PDF Datei mit Bildern zur Gestaltungshilfe. Eine weitere Datei besteht mit allen Verpackungen, die gestaltet werden sollen.
Alle Logos sind auch noch in weiteren Formaten verfügbar.
Vielen Dank im Voraus
Marta & ..

```html
<!DOCTYPE html>
<html lang="de">
<head>
<meta charset="utf-8">
<title>Berardi – Verpackungen Tee und Pasta</title>
<link rel="stylesheet" href="https://fonts.googleapis.com/css2?family=Copse&family=Cormorant+Garamond:wght@500;600&family=Roboto+Mono:wght@700&display=swap">
<style>
  :root {
    --slate: #232323;
    --slate-deep: #151515;
    --kraft: #cdbda2;
    --kraft-light: #dccfb8;
    --ink: #2a2621;
    --chalk: #f4f1ea;
    --organic: #7ab829;
    --olive: #8e8a2c;
    --pasta: #d9ae4c;
  }
  * { box-sizing: border-box; margin: 0; padding: 0; }
  html, body { width: 1200px; height: 1200px; overflow: hidden; background: #ffffff; }
  .canvas { position: relative; width: 1200px; height: 1200px; }

  /* ---------- tea pouch ---------- */
  .tea-pouch {
    position: absolute; left: 124px; top: 252px; width: 460px; height: 684px;
    overflow: hidden; border-radius: 4px;
  }
  .tea-pouch__scene {
    position: absolute; inset: 0;
    background:
      radial-gradient(ellipse at 20% 8%, rgba(142,138,44,.55), transparent 28%),
      radial-gradient(ellipse at 85% 10%, rgba(142,138,44,.45), transparent 25%),
      radial-gradient(ellipse at 95% 42%, rgba(120,110,60,.45), transparent 18%),
      radial-gradient(ellipse at 6% 55%, rgba(60,90,40,.5), transparent 16%),
      radial-gradient(ellipse at 50% 50%, var(--slate), var(--slate-deep));
  }
  .tea-pouch__zip {
    position: absolute; left: 0; right: 0; top: 92px; height: 2px;
    background: rgba(0,0,0,.45); box-shadow: 0 1px 0 rgba(255,255,255,.08);
  }
  .brand-name {
    position: absolute; left: 0; right: 0; text-align: center;
    font-family: "Cormorant Garamond", serif; font-weight: 600;
    color: var(--chalk); letter-spacing: .04em;
  }
  .tea-pouch .brand-name { top: 282px; font-size: 28px; }
  .tea-pouch__title {
    position: absolute; left: 0; right: 0; top: 352px; text-align: center;
    font-family: "Copse", serif; color: var(--chalk);
    font-size: 43px; line-height: 46px; letter-spacing: .04em;
  }
  .tea-pouch__steep {
    position: absolute; left: 0; right: 0; top: 510px; text-align: center;
    font-family: "Cormorant Garamond", serif; font-weight: 500;
    color: var(--chalk); font-size: 15px;
  }
  .kraft-edge { position: absolute; left: 0; width: 100%; }
  .tea-pouch .kraft-edge { top: 540px; height: 144px; }
  .tea-pouch__facts {
    position: absolute; left: 70px; top: 585px; list-style: none;
    font-family: "Copse", serif; color: var(--ink); font-size: 14px; line-height: 18px;
  }
  .tea-pouch__facts li { position: relative; padding-left: 20px; }
  .tea-pouch__facts li::before {
    content: ""; position: absolute; left: 0; top: 6px; width: 13px; height: 5px;
    border-radius: 50%; background: var(--ink);
  }
  .organic-badge { position: absolute; background: var(--organic); }
  .tea-pouch .organic-badge { left: 348px; top: 562px; width: 72px; height: 58px; }
  .net-weight { position: absolute; color: var(--ink); }
  .tea-pouch .net-weight {
    left: 346px; top: 632px; font-family: "Copse", serif; font-size: 22px;
  }

  /* ---------- pasta topper ---------- */
  .pasta-topper {
    position: absolute; left: 693px; top: 260px; width: 385px; height: 334px;
    overflow: hidden;
  }
  .pasta-topper__scene {
    position: absolute; inset: 0;
    background:
      linear-gradient(90deg, rgba(217,174,76,.75) 0, rgba(217,174,76,.25) 15%, transparent 24%),
      linear-gradient(270deg, rgba(217,174,76,.6) 0, rgba(217,174,76,.2) 13%, transparent 22%),
      radial-gradient(ellipse at 50% 40%, #2a2a2a, var(--slate-deep));
  }
  .pasta-topper .brand-name { top: 118px; font-size: 22px; }
  .pasta-topper__title {
    position: absolute; left: 0; right: 0; top: 170px; text-align: center;
    font-family: "Copse", serif; color: var(--chalk); font-size: 40px; letter-spacing: .05em;
  }
  .pasta-topper__cook {
    position: absolute; left: 0; right: 0; top: 220px; text-align: center;
    font-family: "Roboto Mono", monospace; color: var(--chalk); font-size: 9px;
  }
  .pasta-topper .kraft-edge { top: 276px; height: 58px; }
  .pasta-topper .organic-badge { left: 288px; top: 240px; width: 83px; height: 54px; }
  .pasta-topper__facts {
    position: absolute; left: 70px; top: 292px; width: 240px; text-align: center;
    font-family: "Roboto Mono", monospace; color: var(--ink); font-size: 9.5px; line-height: 15px;
  }
  .pasta-topper .net-weight {
    left: 318px; top: 300px; font-family: "Roboto Mono", monospace; font-size: 16px;
  }
</style>
</head>
<body>
<main class="canvas">

  <section class="tea-pouch">
    <div class="tea-pouch__scene" role="img" aria-label="Fotografie: grüne Oliven, Olivenblätter, Ölkännchen und Ölflasche auf dunklem Schiefer"></div>
    <div class="tea-pouch__zip"></div>
    <div class="brand-name">BERARDI</div>
    <h1 class="tea-pouch__title">OLIVEN<br>BLÄTTER<br>TEE</h1>
    <p class="tea-pouch__steep">Wartezeit ca. 5 Minuten</p>
    <svg class="kraft-edge" viewBox="0 0 460 144" preserveAspectRatio="none" aria-hidden="true">
      <path d="M0 30 L40 26 L80 32 L130 24 L180 28 L230 20 L280 22 L330 14 L380 12 L420 6 L460 0 L460 144 L0 144 Z" fill="var(--kraft)"/>
      <path d="M0 30 L40 26 L80 32 L130 24 L180 28 L230 20 L280 22 L330 14 L380 12 L420 6 L460 0" fill="none" stroke="var(--kraft-light)" stroke-width="3"/>
    </svg>
    <ul class="tea-pouch__facts">
      <li>Ohne Zusatz von Aromen</li>
      <li>Von Natur aus rein<br>und koffeinfrei</li>
      <li>Traditionelle Blattmischung</li>
    </ul>
    <div class="organic-badge"></div>
    <div class="net-weight">200g</div>
  </section>

  <section class="pasta-topper">
    <div class="pasta-topper__scene" role="img" aria-label="Fotografie: Tagliatelle-Nester, Tomaten, Basilikum, Mehl und Spaghetti auf dunklem Schiefer"></div>
    <div class="brand-name">BERARDI</div>
    <h2 class="pasta-topper__title">FUSSILI</h2>
    <p class="pasta-topper__cook">Kochzeit ca. 6 Minuten</p>
    <svg class="kraft-edge" viewBox="0 0 385 58" preserveAspectRatio="none" aria-hidden="true">
      <path d="M0 14 L50 10 L100 12 L150 6 L200 8 L250 4 L300 6 L340 2 L385 4 L385 58 L0 58 Z" fill="var(--kraft)"/>
    </svg>
    <div class="organic-badge"></div>
    <p class="pasta-topper__facts">aus Hartweizen<br>mindestens 25% Eier aus Bodenhaltung</p>
    <div class="net-weight">500g</div>
  </section>

</main>
</body>
</html>
```